Flyer for customer acquisition.

Hello, We are a sportmanagement agency from Germany and we need information flyers for customer acquisition. It should be DinA4 and should have a modern but serious design. I have uploaded a information sheet, where you can find the text and the composition, the flyer should have. I also uploaded Pictures / Images, which you can use. Of course you can use other suitable images. If they are not free, I will buy them later. On the bottom of the flyer there has been the contact information. You will find them in the download section, too. If you have questions, just write me. If I forgot something, I will update the letter :) Thank you very much!
Ich brauche zusätzliche Tage um durchzusehen

```html
<!DOCTYPE html>
<html lang="de">
<head>
<meta charset="utf-8">
<title>NOVA-S Flyer – Vorder- und Rückseite</title>
<link rel="stylesheet" href="https://fonts.googleapis.com/css2?family=Anton&family=Montserrat:wght@400;500;600;700&display=swap">
<style>
  :root {
    --canvas: #e3e3e3;
    --ink: #2b2b22;
    --ink-soft: #3b3b30;
    --olive: #5d5a22;
    --olive-light: #9b8f45;
    --gold: #d8c25a;
    --ribbon: #8e2219;
    --tick: #b32b1f;
    --white: #ffffff;
    --footer-dark: #10210d;
    --frame: rgba(80, 70, 40, 0.55);
  }
  * { box-sizing: border-box; margin: 0; padding: 0; }
  html, body { width: 1200px; height: 817px; overflow: hidden; }
  body {
    background: var(--canvas);
    font-family: "Montserrat", Arial, sans-serif;
    color: var(--ink);
    position: relative;
  }
  .flyer-page {
    position: absolute;
    top: 70px;
    width: 482px;
    height: 676px;
    overflow: hidden;
    box-shadow: 0 6px 18px rgba(0,0,0,0.25);
  }
  .flyer-page--front { left: 94px; }
  .flyer-page--back { left: 624px; }

  .stadium-backdrop {
    position: absolute; inset: 0;
    background:
      radial-gradient(ellipse 70% 35% at 50% 38%, rgba(255,250,225,0.95), rgba(255,250,225,0) 70%),
      linear-gradient(180deg, #8d8089 0%, #b3a7a4 10%, #ece3cf 24%, #f6f1d9 40%, #e6ebc6 55%, #b7d27a 68%, #5f9a2e 80%, #2c5e17 92%, #173811 100%);
  }
  .back-glow {
    position: absolute; inset: 0;
    background: radial-gradient(ellipse 60% 30% at 70% 40%, rgba(255,255,255,0.8), rgba(255,255,255,0) 70%);
  }

  .brand-mark {
    position: absolute; top: 40px; left: 0; right: 0;
    display: flex; justify-content: center; align-items: center; gap: 8px;
  }
  .brand-mark__dot {
    width: 14px; height: 14px; border-radius: 50%; background: var(--ink);
  }
  .brand-mark__name {
    font-family: "Montserrat", Arial, sans-serif;
    font-weight: 700; font-size: 28px; letter-spacing: 1px; color: var(--ink);
  }

  .headline {
    position: absolute; left: 0; right: 0; text-align: center;
    font-family: "Anton", Impact, sans-serif; text-transform: uppercase;
  }
  .headline--line1 {
    top: 108px; font-size: 33px; color: #fbf6e6;
    text-shadow: 0 1px 0 #5b4a30, 0 2px 3px rgba(0,0,0,0.45);
  }
  .headline--line2 {
    top: 140px; font-size: 56px; line-height: 1.1;
    background: linear-gradient(180deg, #c4b56a 0%, #7f7632 55%, #4f4a1a 100%);
    -webkit-background-clip: text; background-clip: text; color: transparent;
  }
  .tagline-ribbon {
    position: absolute; top: 207px; left: 74px; width: 330px; height: 18px;
    background: var(--ribbon);
    clip-path: polygon(4% 0, 96% 0, 100% 100%, 0 100%);
    color: var(--white); font-weight: 700; font-size: 10.5px;
    display: flex; align-items: center; justify-content: center; letter-spacing: 0.2px;
  }

  .service-frame {
    position: absolute; border: 1px solid var(--frame); border-radius: 3px;
  }
  .service-frame--front { left: 33px; top: 226px; width: 424px; height: 250px; }
  .service-frame--back { left: 33px; top: 112px; width: 424px; height: 372px; border-right-color: transparent; border-bottom-color: transparent; }

  .service-item { position: absolute; }
  .service-item__title {
    font-weight: 700; font-size: 12px; color: var(--ink); letter-spacing: 0.2px; line-height: 14px;
  }
  .service-item__text {
    font-size: 9.5px; line-height: 12.5px; color: var(--ink-soft); margin-top: 1px;
  }
  .service-item--front { left: 61px; width: 318px; }
  .service-item--front .tick {
    position: absolute; left: -15px; top: 2px; width: 10px; height: 10px;
  }
  .service-item--back { left: 49px; width: 262px; }

  .service-icon { position: absolute; }

  .football {
    position: absolute; border-radius: 50%;
    background: radial-gradient(circle at 38% 32%, #ffffff 0%, #e9e9e9 40%, #9a9a9a 80%, #4a4a4a 100%);
    box-shadow: 0 10px 16px rgba(0,0,0,0.45);
  }
  .football--front { left: 176px; top: 440px; width: 132px; height: 132px; }
  .football--back { left: 310px; top: 492px; width: 80px; height: 80px; }

  .player-splash {
    position: absolute; left: 273px; top: 148px; width: 208px; height: 416px;
    border-radius: 45% 40% 30% 30%;
    background: linear-gradient(160deg, rgba(196,70,150,0.85) 0%, rgba(110,70,170,0.85) 30%, rgba(70,170,210,0.8) 55%, rgba(240,200,60,0.8) 85%, rgba(240,200,60,0) 100%);
    filter: blur(1px);
  }

  .claim {
    position: absolute; left: 41px;
    font-family: "Anton", Impact, sans-serif; text-transform: uppercase; color: #f4f1e6;
    text-shadow: 0 2px 0 #3f3f3f, 0 3px 5px rgba(0,0,0,0.5);
  }
  .claim--line1 { top: 496px; font-size: 44px; line-height: 1.1; }
  .claim--line2 { top: 545px; font-size: 28px; line-height: 1.1; }

  .disclaimer-band {
    position: absolute; left: 26px; top: 594px; width: 430px; height: 40px;
    background: rgba(10, 22, 8, 0.88);
    clip-path: polygon(3% 0, 97% 0, 100% 100%, 0 100%);
    color: #f1f1e6; font-size: 5.3px; line-height: 7px; text-align: center;
    padding: 5px 28px 0;
  }
  .disclaimer-band p + p { margin-top: 3px; }

  .contact-row {
    position: absolute; left: 0; right: 0; top: 640px; height: 26px;
    display: flex; justify-content: center; align-items: center; gap: 16px;
    color: var(--white); font-size: 11px; font-weight: 500;
  }
  .contact-row__item { display: flex; align-items: center; gap: 6px; }
  .contact-row__icon { width: 15px; height: 15px; }
  .bottom-shade {
    position: absolute; left: 0; right: 0; bottom: 0; height: 60px;
    background: linear-gradient(180deg, rgba(12,30,8,0) 0%, rgba(12,30,8,0.85) 100%);
  }
</style>
</head>
<body>

<!-- Front page -->
<section class="flyer-page flyer-page--front">
  <div class="stadium-backdrop" role="img" aria-label="Stadium under a cloudy sky with a green pitch and faded player silhouettes"></div>

  <div class="brand-mark">
    <span class="brand-mark__dot"></span>
    <span class="brand-mark__name">NOVA</span>
  </div>

  <h1 class="headline headline--line1">NOVA-S Nachwuchsförderung</h1>
  <div class="headline headline--line2">und -Mangement</div>
  <div class="tagline-ribbon">WIR BEGLEITEN DICH AUF DEINEM WEG ZUM PROFI</div>

  <div class="service-frame service-frame--front"></div>

  <div class="service-item service-item--front" style="top:248px">
    <svg class="tick" viewBox="0 0 10 10"><circle cx="5" cy="5" r="5" fill="var(--tick)"/><path d="M2.6 5.1 L4.4 6.8 L7.4 3.4" stroke="#fff" stroke-width="1.4" fill="none"/></svg>
    <div class="service-item__title">KARRIEREPLANUNG</div>
    <div class="service-item__text">Wir haben deine Karriere im Blick! In enger Absprache mit deinen Eltern und dir leiten wir die richtigen Maßnahmen und Schritte ein, um dein Ziel „Profifußballer“ zu realisieren.</div>
  </div>

  <div class="service-item service-item--front" style="top:322px">
    <svg class="tick" viewBox="0 0 10 10"><circle cx="5" cy="5" r="5" fill="var(--tick)"/><path d="M2.6 5.1 L4.4 6.8 L7.4 3.4" stroke="#fff" stroke-width="1.4" fill="none"/></svg>
    <div class="service-item__title">STÄNDIGER ANSPRECHPARTNER</div>
    <div class="service-item__text">Egal um welchen Themen es sich handelt, wir sind für dich da! Ein vertrauensvolles und freundschaftliches Verhältnis ist uns besonders wichtig.</div>
  </div>

  <div class="service-item service-item--front" style="top:391px">
    <svg class="tick" viewBox="0 0 10 10"><circle cx="5" cy="5" r="5" fill="var(--tick)"/><path d="M2.6 5.1 L4.4 6.8 L7.4 3.4" stroke="#fff" stroke-width="1.4" fill="none"/></svg>
    <div class="service-item__title">RECHTSBERATUNG/VERTRAGSRECHT</div>
    <div class="service-item__text">Juristendeutsch und Kleingedrucktes? Kein Problem! Wir helfen dir den Durchblick zu behalten und holen immer das Beste für dich raus.</div>
  </div>

  <!-- Steps icon -->
  <svg class="service-icon" style="left:380px;top:244px" width="62" height="62" viewBox="0 0 62 62">
    <path d="M4 58 H22 V46 H34 V34 H46 V22 H58" stroke="var(--olive)" stroke-width="4" fill="none"/>
    <path d="M52 14 L58 20 L52 26" stroke="var(--olive)" stroke-width="3" fill="none"/>
    <rect x="8" y="18" width="8" height="24" rx="3" fill="var(--olive)"/>
    <circle cx="12" cy="10" r="5" fill="var(--olive)"/>
  </svg>

  <!-- Phone + mail icon -->
  <svg class="service-icon" style="left:380px;top:318px" width="58" height="58" viewBox="0 0 58 58">
    <path d="M6 26 C4 14 14 4 28 6 L30 14 L22 16 C20 20 20 26 22 30 L30 32 L30 40 C16 42 8 36 6 26Z" fill="var(--olive)"/>
    <rect x="24" y="26" width="30" height="20" rx="2" fill="#f4efd9" stroke="var(--olive)" stroke-width="2.5"/>
    <path d="M24 27 L39 38 L54 27" stroke="var(--olive)" stroke-width="2.5" fill="none"/>
    <text x="14" y="55" font-family="Montserrat, sans-serif" font-size="14" font-weight="700" fill="var(--olive)">@</text>
  </svg>

  <!-- Scale icon -->
  <svg class="service-icon" style="left:382px;top:386px" width="56" height="56" viewBox="0 0 56 56">
    <rect x="26" y="6" width="4" height="40" fill="var(--olive)"/>
    <rect x="16" y="46" width="24" height="5" fill="var(--olive)"/>
    <rect x="6" y="12" width="44" height="3" fill="var(--olive)"/>
    <circle cx="28" cy="6" r="4" fill="var(--olive)"/>
    <path d="M10 15 L3 32 H17 Z M46 15 L39 32 H53 Z" fill="none" stroke="var(--olive)" stroke-width="2"/>
    <path d="M2 32 H18 C16 38 4 38 2 32Z M38 32 H54 C52 38 40 38 38 32Z" fill="var(--olive)"/>
  </svg>

  <div class="football football--front" role="img" aria-label="Football on the pitch"></div>

  <div class="bottom-shade"></div>
  <div class="disclaimer-band">
    <p>*Die Entscheidung über das Zustandekommen eines Ausrüstervertrags obliegt dem jeweiligen Sportartikelhersteller. Ist ein Abschluss aktuell nicht möglich, erhältst du von uns 2x pro Saison neue Fußballschuhe sowie weitere Ausrüstungsgegenstände.</p>
    <p>**Personal Training, Athletik-Training, Ernährungsberatung, Sportpsychologische Betreuung, uvm.</p>
  </div>
  <div class="contact-row">
    <span class="contact-row__item">
      <svg class="contact-row__icon" viewBox="0 0 16 16"><circle cx="8" cy="8" r="8" fill="var(--gold)"/><path d="M5 4 L7 4 L7.6 6.4 L6.6 7.2 C7.2 8.6 8 9.4 9 9.8 L9.8 8.8 L12 9.4 L12 11.4 C8 12 4.4 8.2 5 4Z" fill="var(--footer-dark)"/></svg>
      07000/5550123
    </span>
    <span class="contact-row__item">
      <svg class="contact-row__icon" viewBox="0 0 16 16"><circle cx="8" cy="8" r="8" fill="var(--gold)"/><rect x="4" y="5" width="8" height="6" fill="var(--footer-dark)"/><path d="M4 5 L8 8.4 L12 5" stroke="var(--gold)" stroke-width="1" fill="none"/></svg>
      info@nova-s.example
    </span>
    <span class="contact-row__item">
      <svg class="contact-row__icon" viewBox="0 0 16 16"><circle cx="8" cy="8" r="8" fill="var(--gold)"/><text x="8" y="10" text-anchor="middle" font-family="Montserrat, sans-serif" font-size="4.5" font-weight="700" fill="var(--footer-dark)">www</text></svg>
      www.nova-s.example
    </span>
  </div>
</section>

<!-- Back page -->
<section class="flyer-page flyer-page--back">
  <div class="stadium-backdrop" role="img" aria-label="Bright stadium under a cloudy sky with a green pitch"></div>
  <div class="back-glow"></div>

  <div class="brand-mark">
    <span class="brand-mark__dot"></span>
    <span class="brand-mark__name">NOVA</span>
  </div>

  <div class="player-splash" role="img" aria-label="Colourful paint-splash illustration of a football player in motion"></div>

  <div class="service-frame service-frame--back"></div>

  <!-- Gear icon -->
  <svg class="service-icon" style="left:48px;top:124px" width="42" height="42" viewBox="0 0 42 42">
    <circle cx="24" cy="21" r="12" fill="none" stroke="var(--olive)" stroke-width="6" stroke-dasharray="5 3"/>
    <circle cx="24" cy="21" r="5" fill="none" stroke="var(--olive)" stroke-width="3"/>
    <rect x="3" y="4" width="6" height="34" rx="2" fill="var(--olive)"/>
  </svg>
  <div class="service-item service-item--back" style="top:172px">
    <div class="service-item__title">AUSRÜSTUNG</div>
    <div class="service-item__text">Wir besorgen dir deine Ausrüstung! Unsere Beziehungen zu den großen Sportartikelherstellern ermöglichen den Abschluss von Ausrüsterverträgen*.</div>
  </div>

  <!-- Hand-stop icon -->
  <svg class="service-icon" style="left:48px;top:232px" width="44" height="44" viewBox="0 0 44 44">
    <circle cx="22" cy="22" r="19" fill="none" stroke="var(--ink)" stroke-width="3"/>
    <rect x="14" y="13" width="4" height="14" rx="2" fill="var(--ink)"/>
    <rect x="19" y="10" width="4" height="16" rx="2" fill="var(--ink)"/>
    <rect x="24" y="12" width="4" height="14" rx="2" fill="var(--ink)"/>
    <rect x="14" y="22" width="16" height="10" rx="4" fill="var(--ink)"/>
  </svg>
  <div class="service-item service-item--back" style="top:280px">
    <div class="service-item__title">VORSORGE</div>
    <div class="service-item__text">Verletzungen gehören leider zum Fußball dazu. Wir sichern dich ab, indem wir eine private Zusatzkrankenversicherung für dich abschließen.</div>
  </div>

  <!-- Network icon -->
  <svg class="service-icon" style="left:50px;top:340px" width="44" height="44" viewBox="0 0 44 44">
    <g stroke="var(--ink)" stroke-width="2.5">
      <line x1="22" y1="22" x2="8" y2="8"/><line x1="22" y1="22" x2="36" y2="8"/>
      <line x1="22" y1="22" x2="8" y2="36"/><line x1="22" y1="22" x2="36" y2="36"/>
      <line x1="22" y1="22" x2="40" y2="22"/>
    </g>
    <circle cx="22" cy="22" r="7" fill="var(--ink)"/>
    <circle cx="8" cy="8" r="5" fill="var(--ink)"/><circle cx="36" cy="8" r="5" fill="var(--ink)"/>
    <circle cx="8" cy="36" r="5" fill="var(--ink)"/><circle cx="36" cy="36" r="5" fill="var(--ink)"/>
    <circle cx="40" cy="22" r="3.5" fill="var(--ink)"/>
  </svg>
  <div class="service-item service-item--back" style="top:393px">
    <div class="service-item__title">KOOPERATIONSPARTNER<br>/NETZWERK</div>
    <div class="service-item__text">Ob Entscheidungsträger oder Experte, wir kennen die richtigen Leute. Zusätzlich bieten wir dir eine große Bandbreite an Leistungen, die du jederzeit in Anspruch nehmen kannst**.</div>
  </div>

  <div class="claim claim--line1">Mit Träumen</div>
  <div class="claim claim--line2">beginnt die Realität</div>

  <div class="football football--back" role="img" aria-label="Football with splashes of grass"></div>

  <div class="bottom-shade"></div>
  <div class="disclaimer-band">
    <p>*Die Entscheidung über das Zustandekommen eines Ausrüstervertrags obliegt dem jeweiligen Sportartikelhersteller. Ist ein Abschluss aktuell nicht möglich, erhältst du von uns 2x pro Saison neue Fußballschuhe sowie weitere Ausrüstungsgegenstände.</p>
    <p>**Personal Training, Athletik-Training, Ernährungsberatung, Sportpsychologische Betreuung, uvm.</p>
  </div>
  <div class="contact-row">
    <span class="contact-row__item">
      <svg class="contact-row__icon" viewBox="0 0 16 16"><circle cx="8" cy="8" r="8" fill="var(--gold)"/><path d="M5 4 L7 4 L7.6 6.4 L6.6 7.2 C7.2 8.6 8 9.4 9 9.8 L9.8 8.8 L12 9.4 L12 11.4 C8 12 4.4 8.2 5 4Z" fill="var(--footer-dark)"/></svg>
      07000/5550123
    </span>
    <span class="contact-row__item">
      <svg class="contact-row__icon" viewBox="0 0 16 16"><circle cx="8" cy="8" r="8" fill="var(--gold)"/><rect x="4" y="5" width="8" height="6" fill="var(--footer-dark)"/><path d="M4 5 L8 8.4 L12 5" stroke="var(--gold)" stroke-width="1" fill="none"/></svg>
      info@nova-s.example
    </span>
    <span class="contact-row__item">
      <svg class="contact-row__icon" viewBox="0 0 16 16"><circle cx="8" cy="8" r="8" fill="var(--gold)"/><text x="8" y="10" text-anchor="middle" font-family="Montserrat, sans-serif" font-size="4.5" font-weight="700" fill="var(--footer-dark)">www</text></svg>
      www.nova-s.example
    </span>
  </div>
</section>

</body>
</html>
```